Business Cards for new orthopaedic surgery practice

My husband and I are starting our own orthopaedic surgery practice. We are looking for a business card that is uniform, but one will have my name/title and the other will have his. You can just create one design with my name on it for now. But when I choose your design as the winning design I will ask that you add another copy with his name/title.

We are looking for classy, simple, elite all in one. We like dark blues/a little gold/yellow. Something that goes with our logo. We want our logo incorporated. Here is all the info you need:
Business name: RV Spine & Vitality Center
Location: 38915 North Bramble Ave
Coral Springs, FL 33071
Phone: 954-218-4630
Fax: 954-571-2846
Email: info@myrvspine.example

Names: Lucinda Ferrow, M.D.
Board Certified Hand and Upper Extremity Surgeon

Emeka Dlunga, M.D.
Board Certified Hip & Knee Replacement/General Orthopaedic Surgeon

Can decide what you want to put on the back. Maybe a slogan:
Rooted in Care. Focused on You

I am just going to upload our logo. The only thing is if we select you as the winning design, the location, and phone numbers may change. We will need your help to update that once fully solidified.

Industry/Entity Type

Medical

Contact Information for Business Card

Colors
0054AA
0677BA
7BADD7
CADEEF
E8F1F8
0094D4
00A9DD
6FCCEA
C7EBF8
E9F6FB

Requirements
Must have
• class, appeal,
Should not have
• We want to air on the side of masculine if we are looking at masculine vs. feminine feel. But we still want it classy, sophisticated, and something we will love

```html
<!DOCTYPE html>
<html lang="en">
<head>
<meta charset="utf-8">
<title>RV Spine &amp; Vitality Center — Business Card</title>
<link href="https://fonts.googleapis.com/css2?family=Raleway:wght@300;400;600&display=swap" rel="stylesheet">
<style>
  :root {
    --page-bg: #dfe6ee;
    --card-bg: #f4f6f9;
    --navy: #1b2859;
    --navy-mid: #22336d;
    --brand-blue: #1d84c4;
    --name-blue: #1a9ad6;
    --title-ink: #dde3ee;
    --contact-ink: #b9bfcc;
    --icon-teal: #2f9a9a;
    --logo-ink: #2a3566;
  }
  html, body {
    margin: 0;
    width: 1200px;
    height: 894px;
    overflow: hidden;
    background: var(--page-bg);
    font-family: "Raleway", Arial, sans-serif;
  }
  .card {
    position: absolute;
    left: 100px;
    top: 164px;
    width: 1000px;
    height: 566px;
    background: var(--card-bg);
    border-radius: 44px;
    overflow: hidden;
    box-shadow: 0 14px 40px rgba(30, 45, 80, 0.18);
  }
  .brand {
    position: absolute;
    left: 50px;
    top: 96px;
    display: flex;
    align-items: center;
    gap: 22px;
  }
  .brand-dot {
    width: 70px;
    height: 70px;
    border-radius: 50%;
    background: var(--logo-ink);
  }
  .brand-name {
    font-weight: 600;
    font-size: 36px;
    line-height: 1.12;
    color: var(--logo-ink);
    letter-spacing: 0.5px;
  }
  .info-band {
    position: absolute;
    left: 0;
    top: 282px;
    width: 100%;
    height: 240px;
    background: linear-gradient(90deg, var(--navy) 0%, var(--navy-mid) 55%, #1f4a8a 75%, var(--brand-blue) 100%);
  }
  .person-name {
    position: absolute;
    left: 42px;
    top: 20px;
    margin: 0;
    font-weight: 600;
    font-size: 31px;
    color: var(--name-blue);
  }
  .person-title {
    position: absolute;
    left: 42px;
    top: 62px;
    margin: 0;
    font-weight: 400;
    font-size: 24px;
    color: var(--title-ink);
  }
  .contacts {
    position: absolute;
    left: 40px;
    top: 118px;
    margin: 0;
    padding: 0;
    list-style: none;
  }
  .contacts li {
    display: flex;
    align-items: center;
    gap: 14px;
    height: 35px;
    font-size: 24px;
    font-weight: 400;
    color: var(--contact-ink);
  }
  .contacts svg { width: 22px; height: 22px; flex: none; }
  .band-mark {
    position: absolute;
    right: 60px;
    top: 20px;
    width: 200px;
    height: 200px;
    border-radius: 50%;
    background: rgba(220, 230, 242, 0.35);
  }
</style>
</head>
<body>
  <main class="card">
    <div class="brand">
      <div class="brand-dot"></div>
      <div class="brand-name">RV Spine &amp;<br>Vitality Center</div>
    </div>

    <section class="info-band">
      <h1 class="person-name">Lucinda Ferrow, M.D.</h1>
      <p class="person-title">Board Certified Hand and Upper Extremity Surgeon</p>
      <ul class="contacts">
        <li>
          <svg viewBox="0 0 22 22" aria-hidden="true"><circle cx="11" cy="11" r="10" fill="var(--icon-teal)"/><path d="M7 8.5c0-1 1-1.5 4-1.5s4 .5 4 1.5v1h-2v-1h-4v1H7z M8 11h6l1 4H7z" fill="var(--navy)"/></svg>
          954-218-4630
        </li>
        <li>
          <svg viewBox="0 0 22 22" aria-hidden="true"><circle cx="11" cy="11" r="10" fill="var(--icon-teal)"/><rect x="7" y="6" width="8" height="4" fill="var(--navy)"/><rect x="6" y="10" width="10" height="6" rx="1" fill="var(--navy)"/></svg>
          954-571-2846
        </li>
        <li>
          <svg viewBox="0 0 22 22" aria-hidden="true"><circle cx="11" cy="11" r="10" fill="var(--icon-teal)"/><rect x="6" y="7.5" width="10" height="7" fill="var(--navy)"/><path d="M6 7.5l5 4 5-4" stroke="var(--icon-teal)" stroke-width="1.2" fill="none"/></svg>
          info@myrvspine.example
        </li>
      </ul>
      <div class="band-mark" aria-hidden="true"></div>
    </section>
  </main>
</body>
</html>
```